Wren Vehicle Polishing (Mobile detail)

I need a business card made up. I'd like it to be different in some form, either raised, embossed, debossed, something cool that stands out. (preferably embossed text somewhere in it). I will be including the Initial png file. Let me know if you need the photoshop of adobe illustrator file to work with.

Information to be included: Text: XXX-XXX-XXXX Phone: XXX-XXX-XXXX Email: wrenpolishcrew@mailbox-demo.net Website: www.socialpage-demo.net/wrenpolishKTR Hours of operation: Mon - Fri 7:00AM to 8:00PM Sat - 10:00AM to 8:00PM

Target Market(s)

Mobile automotive detailing

Industry/Entity Type

Automotive

Contact Information for Business Card

Make it stand out with embossed lettering, I'd also like the background to be glossy black or matte, something that represents a shiny car, black preferred

Requirements
Must have
• A glossy background, or something.
• My logo, pick one of them that best fits your design.
Should not have
• White background,
• something that does not stand out.

```html
<!DOCTYPE html>
<html lang="en">
<head>
<meta charset="utf-8">
<title>Wren Vehicle Polishing — Business Card</title>
<link href="https://fonts.googleapis.com/css2?family=Roboto:wght@400;700;900&family=Kaushan+Script&display=swap" rel="stylesheet">
<style>
  :root {
    --page-bg: #d9d9d9;
    --card-black: #101010;
    --card-sheen: #2e2e2e;
    --accent-orange: #ff6a00;
    --text-white: #f4f4f4;
    --logo-silver: #d6d6d6;
  }
  * { margin: 0; padding: 0; box-sizing: border-box; }
  html, body {
    width: 1200px; height: 1200px; overflow: hidden;
    background: var(--page-bg);
    font-family: "Roboto", Arial, sans-serif;
  }
  .sheet {
    width: 1200px; height: 1200px;
    display: flex; flex-direction: column; align-items: center; justify-content: center;
    gap: 60px;
  }
  .card {
    position: relative;
    width: 900px; height: 514px;
    border-radius: 30px;
    overflow: hidden;
    background: var(--card-black);
    box-shadow: 0 14px 30px rgba(0,0,0,.35);
  }
  .card-surface {
    position: absolute; inset: 0;
    background:
      radial-gradient(ellipse at 42% 40%, var(--card-sheen) 0%, rgba(0,0,0,0) 55%),
      linear-gradient(120deg, #0b0b0b 0%, #1c1c1c 45%, #0d0d0d 100%);
  }

  /* Front */
  .front-logo {
    position: absolute; left: 0; right: 0; top: 50%;
    transform: translateY(-50%);
    display: flex; align-items: center; justify-content: center; gap: 20px;
  }
  .logo-dot {
    width: 56px; height: 56px; border-radius: 50%;
    background: var(--accent-orange);
    flex: none;
  }
  .logo-name {
    font-weight: 900;
    color: var(--logo-silver);
    font-size: 50px;
    line-height: 1.05;
    letter-spacing: .5px;
  }

  /* Back */
  .back-logo {
    position: absolute; left: 60px; top: 110px;
    display: flex; align-items: center; gap: 14px;
    width: 300px;
  }
  .back-logo .logo-dot { width: 36px; height: 36px; }
  .back-logo .logo-name { font-size: 32px; }

  .divider-line {
    position: absolute; left: 250px; top: 258px;
    width: 280px; height: 2px;
    background: var(--accent-orange);
  }
  .staff-block {
    position: absolute; right: 44px; top: 150px;
    text-align: right; color: var(--text-white);
  }
  .staff-name {
    font-family: "Kaushan Script", cursive;
    font-size: 44px; line-height: 1;
    margin-bottom: 14px;
  }
  .hours-title {
    color: var(--accent-orange);
    font-weight: 700; font-size: 24px;
    margin-bottom: 8px;
  }
  .hours-line { font-size: 23px; line-height: 1.45; }

  .contact-list {
    position: absolute; left: 230px; top: 300px;
    list-style: none; color: var(--text-white);
    font-size: 22px;
  }
  .contact-list li {
    display: flex; align-items: center; gap: 14px;
    height: 38px;
  }
  .contact-icon { width: 20px; height: 20px; flex: none; }

  .card-footer {
    position: absolute; left: 0; bottom: 0;
    width: 900px; height: 110px;
  }
</style>
</head>
<body>
<main class="sheet">

  <section class="card card-front" aria-label="Card front">
    <div class="card-surface" role="img" aria-label="Glossy black honeycomb carbon texture"></div>
    <div class="front-logo">
      <span class="logo-dot"></span>
      <span class="logo-name">Wren Vehicle Polishing</span>
    </div>
  </section>

  <section class="card card-back" aria-label="Card back">
    <div class="card-surface" role="img" aria-label="Glossy black honeycomb carbon texture"></div>

    <div class="back-logo">
      <span class="logo-dot"></span>
      <span class="logo-name">Wren Vehicle Polishing</span>
    </div>

    <div class="divider-line"></div>

    <div class="staff-block">
      <p class="staff-name">Your Name</p>
      <p class="hours-title">Hours of operation:</p>
      <p class="hours-line">Mon - Fri 7:00AM to 8:00PM</p>
      <p class="hours-line">Sat - 10:00AM to 8:00PM</p>
    </div>

    <ul class="contact-list">
      <li>
        <svg class="contact-icon" viewBox="0 0 20 20" aria-hidden="true">
          <path fill="#ff6a00" d="M4 2h4l1.5 4-2.2 1.6a10 10 0 0 0 5.1 5.1L14 10.5l4 1.5v4a2 2 0 0 1-2 2A14 14 0 0 1 2 4a2 2 0 0 1 2-2z"/>
        </svg>
        <span>XXX-XXX-XXXX</span>
      </li>
      <li>
        <svg class="contact-icon" viewBox="0 0 20 20" aria-hidden="true">
          <rect x="1" y="4" width="18" height="12" rx="1.5" fill="#ff6a00"/>
          <path d="M2 5l8 6 8-6" fill="none" stroke="#101010" stroke-width="1.6"/>
        </svg>
        <span>wrenpolishcrew@mailbox-demo.net</span>
      </li>
      <li>
        <svg class="contact-icon" viewBox="0 0 20 20" aria-hidden="true">
          <rect x="2" y="2" width="16" height="16" rx="2" fill="#ff6a00"/>
        </svg>
        <span>/wrenpolishKTR</span>
      </li>
    </ul>

    <svg class="card-footer" viewBox="0 0 900 110" aria-hidden="true">
      <defs>
        <linearGradient id="silverStrip" x1="0" y1="0" x2="0" y2="1">
          <stop offset="0" stop-color="#f2f2f2"/>
          <stop offset=".45" stop-color="#9a9a9a"/>
          <stop offset=".7" stop-color="#e6e6e6"/>
          <stop offset="1" stop-color="#6f6f6f"/>
        </linearGradient>
      </defs>
      <path d="M560 2 H900 V66 H545 Z" fill="#ff6a00"/>
      <path d="M0 78 H520 L545 66 H900 V110 H0 Z" fill="url(#silverStrip)"/>
    </svg>
  </section>

</main>
</body>
</html>
```